TRQ Harbor Gym Team starting a weekly fitness and wellness podcast.

We need to design both a program advert poster for socials and campaigns as well as a podcast placeholder/poster.
The podcast is part of an online group training program called "Summit Stride".
The four pillars of Summit Stride are Fitness, Nutrition, Mindset & Community.
The program is designed and owned by TRQ Harbor Gym.
The brand guidelines are similar to TRQ Harbor Gym (Attached).
Target Market(s)
People aged between 30 and 60yrs old new or returning to fitness and wellness
Industry/Entity Type
Fitness
Colors
Designer to choose colors to be used in the design.
Requirements
Must have
- A strong motivational appeal. One that inspires and motivates people to take action.
Nice to have
- a captivating caption
Should not have
- Too much Zen or yoga themes.

```html
<!DOCTYPE html>
<html lang="en">
<head>
<meta charset="UTF-8">
<title>Summit Stride Podcast</title>
<link href="https://fonts.googleapis.com/css2?family=Saira+Stencil+One&family=Oswald:wght@400&family=Barlow+Semi+Condensed:wght@600&display=swap" rel="stylesheet">
<style>
  :root {
    --teal: #2e5c5d;
    --teal-deep: #264f50;
    --orange: #e69843;
    --pink: #e0517f;
    --gold: #d7a84f;
    --white: #ffffff;
    --label-text: #f6dde5;
  }
  html, body {
    margin: 0;
    padding: 0;
    overflow: hidden;
    background: var(--teal-deep);
  }
  .poster {
    position: relative;
    width: 1200px;
    height: 1200px;
    overflow: hidden;
    background: radial-gradient(ellipse at 35% 40%, #336465 0%, var(--teal) 55%, var(--teal-deep) 100%);
  }
  .color-shapes {
    position: absolute;
    inset: 0;
  }
  .waveform {
    position: absolute;
    left: 0;
    top: 700px;
    width: 860px;
    height: 200px;
  }
  .microphone {
    position: absolute;
    left: 800px;
    top: 380px;
    width: 360px;
    height: 820px;
    border-radius: 90px 90px 0 0;
    background: linear-gradient(90deg, #5b5b5b 0%, #c9c6c2 35%, #efece8 50%, #a9a6a2 70%, #3e3e3e 100%);
  }
  .title {
    position: absolute;
    left: 50px;
    top: 255px;
    margin: 0;
    font-family: "Saira Stencil One", sans-serif;
    font-weight: 400;
    color: var(--white);
    line-height: 0.98;
    letter-spacing: 2px;
  }
  .title .line-one {
    display: block;
    font-size: 150px;
  }
  .title .line-two {
    display: block;
    font-size: 150px;
    padding-left: 128px;
  }
  .pillars {
    position: absolute;
    left: 106px;
    top: 642px;
    width: 588px;
    height: 82px;
    background: var(--pink);
    display: flex;
    align-items: center;
    justify-content: center;
    font-family: "Oswald", sans-serif;
    font-size: 33px;
    letter-spacing: 0.5px;
    color: var(--label-text);
  }
  .cta {
    position: absolute;
    left: 228px;
    top: 938px;
    width: 372px;
    text-align: center;
    font-family: "Barlow Semi Condensed", sans-serif;
    font-weight: 600;
    font-size: 76px;
    letter-spacing: 2px;
    color: var(--gold);
    padding-bottom: 6px;
    border-bottom: 3px solid var(--label-text);
  }
</style>
</head>
<body>
<main class="poster">
  <svg class="color-shapes" width="1200" height="1200" viewBox="0 0 1200 1200">
    <path class="shape-orange" fill="var(--orange)" d="M930 0 C820 160 780 420 820 640 C840 760 880 860 920 900 L1200 900 L1200 0 Z"/>
    <path class="shape-pink" fill="var(--pink)" d="M1200 210 C990 300 860 520 870 760 C876 930 905 1080 930 1200 L1200 1200 Z"/>
  </svg>

  <svg class="waveform" viewBox="0 0 860 200" fill="var(--gold)" aria-hidden="true">
    <rect x="0" y="70" width="6" height="60"/><rect x="14" y="80" width="6" height="40"/><rect x="28" y="60" width="6" height="80"/><rect x="42" y="75" width="6" height="50"/><rect x="56" y="85" width="6" height="30"/>
    <rect x="70" y="65" width="6" height="70"/><rect x="84" y="50" width="6" height="100"/><rect x="98" y="35" width="6" height="130"/><rect x="112" y="55" width="6" height="90"/><rect x="126" y="30" width="6" height="140"/>
    <rect x="140" y="45" width="6" height="110"/><rect x="154" y="65" width="6" height="70"/><rect x="168" y="78" width="6" height="44"/><rect x="182" y="88" width="6" height="24"/><rect x="196" y="70" width="6" height="60"/>
    <rect x="210" y="55" width="6" height="90"/><rect x="224" y="38" width="6" height="124"/><rect x="238" y="50" width="6" height="100"/><rect x="252" y="25" width="6" height="150"/><rect x="266" y="45" width="6" height="110"/>
    <rect x="280" y="62" width="6" height="76"/><rect x="294" y="80" width="6" height="40"/><rect x="308" y="88" width="6" height="24"/><rect x="322" y="76" width="6" height="48"/><rect x="336" y="60" width="6" height="80"/>
    <rect x="350" y="48" width="6" height="104"/><rect x="364" y="62" width="6" height="76"/><rect x="378" y="40" width="6" height="120"/><rect x="392" y="30" width="6" height="140"/><rect x="406" y="52" width="6" height="96"/>
    <rect x="420" y="70" width="6" height="60"/><rect x="434" y="84" width="6" height="32"/><rect x="448" y="74" width="6" height="52"/><rect x="462" y="58" width="6" height="84"/><rect x="476" y="42" width="6" height="116"/>
    <rect x="490" y="28" width="6" height="144"/><rect x="504" y="46" width="6" height="108"/><rect x="518" y="20" width="6" height="160"/><rect x="532" y="40" width="6" height="120"/><rect x="546" y="58" width="6" height="84"/>
    <rect x="560" y="74" width="6" height="52"/><rect x="574" y="86" width="6" height="28"/><rect x="588" y="70" width="6" height="60"/><rect x="602" y="52" width="6" height="96"/><rect x="616" y="36" width="6" height="128"/>
    <rect x="630" y="56" width="6" height="88"/><rect x="644" y="44" width="6" height="112"/><rect x="658" y="66" width="6" height="68"/><rect x="672" y="80" width="6" height="40"/><rect x="686" y="88" width="6" height="24"/>
    <rect x="700" y="72" width="6" height="56"/><rect x="714" y="58" width="6" height="84"/><rect x="728" y="46" width="6" height="108"/><rect x="742" y="62" width="6" height="76"/><rect x="756" y="78" width="6" height="44"/>
    <rect x="770" y="68" width="6" height="64"/><rect x="784" y="84" width="6" height="32"/><rect x="798" y="74" width="6" height="52"/><rect x="812" y="86" width="6" height="28"/><rect x="826" y="80" width="6" height="40"/>
  </svg>

  <div class="microphone" role="img" aria-label="Studio condenser microphone in a black shock mount"></div>

  <h1 class="title">
    <span class="line-one">SUMMIT</span>
    <span class="line-two">STRIDE</span>
  </h1>

  <div class="pillars">FITNESS, NUTRITION, MINDSET, COMMUNITY</div>

  <div class="cta">JOIN NOW</div>
</main>
</body>
</html>
```